Need a Modern Website!

We would like to optimize our teams website to a strikingly modern fashionable apparel aesthetic.

The brand is about positivity, peace, loving others and embracing diversity.

OUR current website is www.brevontwear.com, all done through cartvane free theme builder.
We’ve have had someone create this site through Gigsly in the past and Cartvane locked our page because creator used an illegal paid theme.

Our website needs an updated MODERN user friendly style, a fresh look like some of the other big people in the apparel. We would like to really stand out and create a unique Home Screen as well as the ABOUT US page.

Pictoram is @brevontwearshop if you need extra photo references and pictures. We can also attach photos to a message, email, or chat.

Below are some sites for solely inspiration.
https://www.krmtpslo.com/
https://www.stayquitegentle.com/

We are Open to all ideas!

Target Market(s)

Women and Men 18-35

Industry/Entity Type

E-Commerce High Quality Apparel

Coding

Coded - Design and coding required

Number of Pages Required

5+ page

Font styles to use
Sans Serif

Colors

Designer to choose colors to be used in the design.

Requirements
Must have
• User friendly experience, modern look, legible fonts,
Nice to have
• colors - navy blue, red, white, black, olive. can use filler photos from free photo site or request our mock-ups.
Should not have
• Nothing gimmicky and youthful.

```html
<!DOCTYPE html>
<html lang="en">
<head>
<meta charset="utf-8">
<title>Brevont Wear — Home</title>
<link href="https://fonts.googleapis.com/css2?family=Inter:wght@400;500;700;800&family=Courgette&display=swap" rel="stylesheet">
<style>
:root{
  --olive:#93a87a;
  --olive-dark:#7d9365;
  --ink:#111111;
  --text:#222222;
  --muted:#5a5a5a;
  --tile:#e7e7e7;
  --white:#ffffff;
  --footer:#050505;
}
*{box-sizing:border-box;margin:0;padding:0}
html,body{width:1200px;height:3622px;overflow:hidden}
body{position:relative;font-family:"Inter",Arial,sans-serif;color:var(--text);background:var(--white)}
.abs{position:absolute}
.announcement{left:0;top:0;width:1200px;height:33px;background:var(--olive);color:#fff;font-size:12.5px;display:flex;align-items:center;justify-content:center}
.site-header{left:0;top:33px;width:1200px;height:136px;background:#fff;border-bottom:1px solid #e5e5e5}
.brand{position:absolute;left:0;width:1200px;top:26px;display:flex;align-items:center;justify-content:center;gap:10px;font-weight:800;font-size:22px;letter-spacing:2px;color:var(--ink)}
.brand-mark{width:16px;height:16px;border-radius:50%;background:var(--ink)}
.header-icons{position:absolute;right:60px;top:32px;display:flex;gap:14px}
.main-nav{position:absolute;top:101px;left:0;width:1200px;display:flex;justify-content:center;gap:30px;font-size:12.5px;color:#555}
.main-nav .active{color:var(--ink)}
.btn{display:flex;align-items:center;justify-content:center;background:var(--olive);color:#fff;font-size:14px;border-radius:4px;letter-spacing:.3px}
.photo{position:absolute}
.hero{left:0;top:169px;width:1200px;height:543px;overflow:hidden}
.hero-shade{position:absolute;inset:0;background:rgba(0,0,0,.28)}
.hero-title{position:absolute;top:190px;width:1200px;text-align:center;color:#fff;font-weight:700;font-size:56px}
.hero-sub{position:absolute;top:268px;width:1200px;text-align:center;color:#fff;font-size:15px}
.hoodies{left:0;top:712px;width:1200px;height:544px;overflow:hidden}
.tear-banner{position:absolute;left:345px;top:870px;width:560px;height:180px;transform:rotate(-8deg);transform-origin:center}
.tear-banner .paper{position:absolute;inset:0;background:#fff;clip-path:polygon(2% 20%,30% 12%,60% 6%,96% 0%,100% 55%,92% 70%,60% 82%,30% 92%,4% 100%,0% 60%)}
.tear-banner .script{position:absolute;left:185px;top:28px;font-family:"Courgette",cursive;font-size:22px;color:var(--olive-dark)}
.tear-banner .title{position:absolute;left:125px;top:58px;font-weight:800;font-size:46px;color:var(--ink)}
.tear-banner .btn{position:absolute;left:205px;top:124px;width:138px;height:36px;border-radius:8px;font-size:14px}
.intro{left:0;top:1256px;width:1200px;height:297px;text-align:center}
.intro h2{position:absolute;top:82px;width:1200px;font-size:34px;font-weight:700;color:var(--ink)}
.intro p{position:absolute;top:140px;left:300px;width:600px;font-size:15px;line-height:26px;color:var(--muted)}
.womens{left:0;top:1553px;width:1200px;height:543px;overflow:hidden}
.badge{position:absolute;left:456px;top:1653px;width:304px;height:304px;border-radius:50%;background:#fff;border:12px solid #fff;box-shadow:0 0 0 0 transparent}
.badge .ring{position:absolute;inset:6px;border-radius:50%;border:8px solid var(--olive)}
.badge h3{position:absolute;top:78px;width:100%;text-align:center;font-size:46px;line-height:48px;font-weight:700;color:var(--ink)}
.badge .btn{position:absolute;left:74px;top:177px;width:134px;height:42px}
.featured-title{left:0;top:2166px;width:1200px;text-align:center;font-size:36px;font-weight:700;color:var(--ink)}
.product{position:absolute;width:300px;text-align:center}
.product .img{width:300px;height:345px;background:var(--tile)}
.product .name{margin-top:32px;font-size:14.5px;color:#444}
.product .price{margin-top:9px;font-size:14.5px;font-weight:700;color:var(--ink)}
.site-footer{left:0;top:3233px;width:1200px;height:389px;background:var(--footer);color:#ccc}
.subscribe-title{position:absolute;top:62px;width:1200px;text-align:center;font-size:20px;color:var(--olive)}
.email-field{position:absolute;left:345px;top:120px;width:509px;height:42px;border:1px solid #ddd;border-radius:4px;font-size:11px;color:#bbb;padding:13px 14px}
.email-field .btn{position:absolute;right:2px;top:2px;width:128px;height:36px;font-size:15px}
.payments{position:absolute;top:213px;left:0;width:1200px;display:flex;justify-content:center;gap:6px}
.payments span{width:44px;height:28px;background:#fff;border-radius:4px}
.footer-links{position:absolute;top:260px;width:1200px;display:flex;justify-content:center;gap:19px;font-size:12px;color:#ccc}
.footer-rule{position:absolute;left:60px;top:331px;width:1080px;height:1px;background:#2a2a2a}
.region{position:absolute;left:61px;top:354px;font-size:11px;color:#aaa}
.region-select{position:absolute;left:153px;top:346px;width:166px;height:32px;border:1px solid #666;font-size:11px;color:#ddd;padding:9px 12px}
.region-select svg{position:absolute;right:10px;top:11px}
.copyright{position:absolute;right:62px;top:355px;font-size:11.5px;color:#ccc}
</style>
</head>
<body>

<div class="abs announcement">Free Shipping On All Orders To Totaling $50 OR More</div>

<header class="abs site-header">
  <div class="brand"><span class="brand-mark"></span>BREVONT WEAR</div>
  <div class="header-icons">
    <svg width="22" height="22" viewBox="0 0 22 22" fill="none" stroke="#111" stroke-width="1.8"><circle cx="9" cy="9" r="6.5"/><line x1="14" y1="14" x2="20" y2="20"/></svg>
    <svg width="22" height="22" viewBox="0 0 22 22" fill="none" stroke="#111" stroke-width="1.6"><circle cx="11" cy="11" r="9.5"/><circle cx="11" cy="8.5" r="3.2"/><path d="M5 17.5c1.5-3 3.5-4 6-4s4.5 1 6 4"/></svg>
    <svg width="24" height="22" viewBox="0 0 24 22" fill="none" stroke="#111" stroke-width="1.6"><path d="M1 2h4l3 12h12l2-9H7"/><circle cx="9.5" cy="18.5" r="1.6"/><circle cx="18" cy="18.5" r="1.6"/></svg>
  </div>
  <nav class="main-nav">
    <span class="active">Home</span>
    <span>Products <svg width="10" height="6" viewBox="0 0 10 6" fill="none" stroke="#777"><path d="M1 1l4 4 4-4"/></svg></span>
    <span>About Us</span><span>Contact Us</span><span>Faq's</span><span>Blogs</span>
  </nav>
</header>

<section class="abs hero">
  <div class="photo" role="img" aria-label="Red embroidered baseball cap" style="left:0;top:0;width:360px;height:543px;background:linear-gradient(160deg,#5a2428,#2b2b2b)"></div>
  <div class="photo" role="img" aria-label="Model in red jacket and ripped jeans seated on a red doorstep" style="left:360px;top:0;width:480px;height:543px;background:linear-gradient(180deg,#5b1c22,#4a3b3a 55%,#3a2e2b)"></div>
  <div class="photo" role="img" aria-label="Woman wearing a red hoodie" style="left:840px;top:0;width:360px;height:543px;background:linear-gradient(180deg,#2e2e2e,#6a1a20 45%,#2a2c38)"></div>
  <div class="hero-shade"></div>
  <h1 class="hero-title">Peace. Love . Brevont</h1>
  <p class="hero-sub">We are all powerful in our own way.</p>
  <div class="btn abs" style="left:532px;top:309px;width:135px;height:45px">SHOP ALL</div>
</section>

<section class="abs hoodies">
  <div class="photo" role="img" aria-label="Man in an olive green hoodie on a city street" style="left:0;top:0;width:656px;height:544px;background:linear-gradient(135deg,#4a4540,#6d7358 55%,#3c3a36)"></div>
  <div class="photo" role="img" aria-label="Man in a sherpa jacket and brown hoodie by the water" style="left:656px;top:0;width:544px;height:544px;background:linear-gradient(160deg,#3aa3a6,#2b3a3a 55%,#4a3a30)"></div>
</section>
<div class="tear-banner">
  <div class="paper"></div>
  <div class="script">Featurte Collection</div>
  <div class="title">Men's Hoodies</div>
  <div class="btn">SHOP ALL</div>
</div>

<section class="abs intro">
  <h2>Once you find peace, you find yourself.</h2>
  <p>This brand is about living out life to the fullest. Brevont Wear is about inclusion, spreading PEACE, encouraging LOVE, and UNIFYING by enjoying the differences in one another.</p>
</section>

<section class="abs womens">
  <div class="photo" role="img" aria-label="Woman with glasses in a black logo t-shirt" style="left:0;top:0;width:600px;height:543px;background:linear-gradient(150deg,#3a2a22,#1d1b1a 60%,#2b2624)"></div>
  <div class="photo" role="img" aria-label="Woman in a royal blue t-shirt seated on a leather sofa" style="left:600px;top:0;width:600px;height:543px;background:linear-gradient(160deg,#4a3e34,#2a2f6a 55%,#3a2a22)"></div>
</section>
<div class="badge">
  <div class="ring"></div>
  <h3>Women's<br>T-Shirts</h3>
  <div class="btn">SHOP ALL</div>
</div>

<h2 class="abs featured-title">Featured Products</h2>

<div class="product" style="left:0;top:2255px"><div class="img" role="img" aria-label="Military green hoodie with graphic print" style="background:radial-gradient(circle at 50% 50%,#4f5a44 0 32%,#fff 33%)"></div><div class="name">Peace is the new Luxury Hoodie</div><div class="price">$32.99 USD</div></div>
<div class="product" style="left:300px;top:2255px"><div class="img" role="img" aria-label="Black long sleeve shirt" style="background:radial-gradient(circle at 50% 50%,#151515 0 32%,var(--tile) 33%)"></div><div class="name">Onyx long Sleeve</div><div class="price">$25.99 USD</div></div>
<div class="product" style="left:600px;top:2255px"><div class="img" role="img" aria-label="Military green long sleeve shirt" style="background:radial-gradient(circle at 50% 50%,#4c4f3c 0 32%,var(--tile) 33%)"></div><div class="name">Miliatry Green Long Sleeve</div><div class="price">$25.99 USD</div></div>
<div class="product" style="left:900px;top:2255px"><div class="img" role="img" aria-label="Royal blue long sleeve shirt" style="background:radial-gradient(circle at 50% 50%,#1f56c4 0 32%,var(--tile) 33%)"></div><div class="name">Royal Blue Long Sleeve</div><div class="price">$25.99 USD</div></div>

<div class="product" style="left:0;top:2743px"><div class="img" role="img" aria-label="Red long sleeve shirt" style="background:radial-gradient(circle at 50% 50%,#e3202a 0 30%,#fff 31%)"></div><div class="name">Red Long Sleeve</div><div class="price">$25.99 USD</div></div>
<div class="product" style="left:300px;top:2743px"><div class="img" role="img" aria-label="Military green hoodie" style="background:radial-gradient(circle at 50% 50%,#5b5f49 0 32%,var(--tile) 33%)"></div><div class="name">Military Green Hoodie</div><div class="price">$32.99 USD</div></div>
<div class="product" style="left:600px;top:2743px"><div class="img" role="img" aria-label="Black hoodie with yellow print" style="background:radial-gradient(circle at 50% 50%,#141414 0 32%,var(--tile) 33%)"></div><div class="name">Black and Yellow Hoodie</div><div class="price">$32.99 USD</div></div>
<div class="product" style="left:900px;top:2743px"><div class="img" role="img" aria-label="Black hoodie with peace and heart graphic" style="background:radial-gradient(circle at 50% 50%,#111 0 34%,#fff 35%)"></div><div class="name">Peace Love brevont Black Hoodie</div><div class="price">$32.99 USD</div></div>

<footer class="abs site-footer">
  <div class="subscribe-title">Subscribe to our Emails</div>
  <div class="email-field">Email *<div class="btn">SUBSCRIBE</div></div>
  <div class="payments" aria-label="Accepted payment methods">
    <span></span><span></span><span></span><span></span><span></span><span></span><span></span><span></span><span></span>
  </div>
  <div class="footer-links"><span>FAQ's</span><span>Contact Us</span><span>Our Refund Policy</span><span>Our Privacy Policy</span><span>Terms of Services</span></div>
  <div class="footer-rule"></div>
  <div class="region">Country / Region</div>
  <div class="region-select">United States (USD $)<svg width="10" height="6" viewBox="0 0 10 6" fill="none" stroke="#ddd"><path d="M1 1l4 4 4-4"/></svg></div>
  <div class="copyright">©2023 Brevont Wear Store - All rights reserved.</div>
</footer>

</body>
</html>
```